Veterinary TPLO Surgery Flyer Design

Please use this flyer to make a professional-looking 1 page, double-sided client handout regarding TPLO.

You can visit our website at www.brookferrypetcare.com & www.northgroveanimalsurgery.com for additional logo information. The flyer should include all the text from the one provided.

Target Market(s)

Client communication to for referral surgery between sister veterinary clinics

Industry/Entity Type

Veterinary

Requirements
Must have
• The text included
Nice to have
• Nice to have the Willow Crest Avenue Animal CLinic & Dr. Pettigrew Mobile vet logos incorporated.

```html
<!DOCTYPE html>
<html lang="en">
<head>
<meta charset="utf-8">
<title>TPLO Surgery Client Handout</title>
<link href="https://fonts.googleapis.com/css2?family=Oswald:wght@600;700&family=Roboto+Slab:wght@300;400&family=Poppins:wght@400;500;600&display=swap" rel="stylesheet">
<style>
:root{
  --bg:#e6e0d8;
  --paper:#ffffff;
  --green:#5e8a70;
  --green-dark:#4d7760;
  --green-soft:#a9c6b2;
  --green-pale:#e6efe8;
  --gold:#d1a83a;
  --ink:#2f3a34;
  --muted:#5b665f;
  --ghost:#eef1ef;
}
*{box-sizing:border-box;margin:0;padding:0}
html,body{width:1200px;height:2588px;overflow:hidden}
body{background:var(--bg);font-family:"Poppins",sans-serif;color:var(--ink);position:relative}
.page{position:absolute;left:160px;width:880px;height:1240px;background:var(--paper);overflow:hidden;box-shadow:0 6px 24px rgba(0,0,0,.08)}
.page--front{top:36px}
.page--back{top:1312px}

.brand{position:absolute;left:52px;top:40px;display:flex;align-items:center;gap:10px;z-index:3}
.brand__mark{width:26px;height:26px;background:var(--green)}
.brand__name{font-family:"Roboto Slab",serif;font-weight:400;font-size:17px;line-height:1.15;color:var(--green-dark);width:200px}
.brand-band{position:absolute;left:0;top:30px;width:330px;height:54px;background:linear-gradient(90deg,var(--green-pale),rgba(230,239,232,0))}
.badge{position:absolute;right:48px;top:30px;width:88px;height:62px;border-radius:10px;background:var(--green-pale);border:2px solid var(--green-soft)}

.bubble{position:absolute;border-radius:50%;background:var(--green)}
.bubble--soft{background:var(--ghost)}

.hero-title{position:absolute;left:40px;top:128px;width:400px;height:400px;border-radius:50%;background:var(--green);z-index:2;padding:110px 0 0 60px}
.hero-title h1{font-family:"Oswald",sans-serif;font-weight:700;font-size:60px;line-height:1.02;color:#fff;letter-spacing:1px}
.hero-title h1 .accent{color:var(--gold)}
.hero-title p{font-family:"Roboto Slab",serif;font-weight:300;font-size:28px;line-height:1.1;color:#f0f4f1;margin-top:12px}
.photo{position:absolute;border-radius:50%;z-index:1}
.photo--dogs{left:380px;top:120px;width:400px;height:400px;background:radial-gradient(circle at 50% 60%,#d8b27a 0,#c99a5c 28%,#8fb39b 60%,#a9c6b2 100%)}

.content{position:absolute;left:58px;right:58px}
.lead{font-family:"Poppins",sans-serif;font-weight:600;font-size:16px;line-height:1.35;color:var(--gold)}
.lead--green{color:var(--green-dark)}
.cols{display:flex;gap:26px;margin-top:22px}
.col{flex:1}
.col + .col{border-left:2px solid var(--green-soft);padding-left:22px}
.sec-h{display:flex;align-items:center;gap:8px;font-weight:600;font-size:14px;color:var(--green-dark);margin:0 0 6px}
.sec-h svg{flex:none}
.body{font-size:10.5px;line-height:1.55;color:var(--muted);margin-bottom:16px;padding-left:24px}
.benefit{margin:0 0 14px 24px}
.benefit h4{font-size:12px;font-weight:600;color:var(--green-dark)}
.benefit p{font-size:10.5px;line-height:1.5;color:var(--muted)}
.xrays{display:flex;gap:10px;margin-left:24px}
.xray{width:110px;height:70px;border-radius:6px;background:linear-gradient(135deg,#3a3f42,#8c9397)}
.xray--light{background:linear-gradient(135deg,#c8cfd2,#eef0f1)}

.footer{position:absolute;left:0;right:0;bottom:0;height:92px;background:var(--green);display:flex;align-items:center;justify-content:space-around;padding:0 30px}
.footer__item{display:flex;align-items:center;gap:8px;font-size:9.5px;line-height:1.4;color:#fff}
.footer__icon{width:24px;height:24px;border-radius:50%;background:rgba(255,255,255,.2);display:flex;align-items:center;justify-content:center;flex:none}

.photo--surgery{left:40px;top:120px;width:420px;height:420px;background:radial-gradient(circle at 45% 45%,#8fb39b,#5e8a70 60%,#4d7760);z-index:2;opacity:.95}
.photo--paw{left:400px;top:120px;width:420px;height:420px;background:radial-gradient(circle at 60% 40%,#f3d3a8,#d99b62 45%,#8b5a3a 100%)}
.intro{font-size:12px;line-height:1.6;color:var(--muted);margin:6px 0 0 24px}
.process{display:grid;grid-template-columns:1fr 1fr 1fr;gap:14px 22px;margin-top:12px}
.step{display:flex;gap:10px}
.step__icon{width:34px;height:34px;border-radius:50%;border:2px solid var(--green-soft);flex:none;display:flex;align-items:center;justify-content:center}
.step h4{font-size:12px;font-weight:600;color:var(--green-dark)}
.step p{font-size:10px;line-height:1.45;color:var(--muted)}
.postop p{font-size:11px;line-height:1.6;color:var(--muted);margin-left:24px}
.postop b{color:var(--ink);font-weight:600}
</style>
</head>
<body>

<!-- FRONT -->
<section class="page page--front">
  <div class="brand-band"></div>
  <div class="brand"><span class="brand__mark"></span><span class="brand__name">Willow Crest Avenue Animal Clinic</span></div>
  <div class="badge" aria-hidden="true"></div>

  <span class="bubble" style="left:440px;top:60px;width:46px;height:46px"></span>
  <span class="bubble" style="left:488px;top:36px;width:30px;height:30px"></span>
  <span class="bubble" style="left:416px;top:100px;width:22px;height:22px"></span>
  <span class="bubble bubble--soft" style="left:730px;top:520px;width:120px;height:120px"></span>
  <span class="bubble bubble--soft" style="left:40px;top:1030px;width:90px;height:90px"></span>

  <div class="hero-title">
    <h1>ADVANCED<br><span class="accent">ORTHOPEDIC</span><br>CARE</h1>
    <p>At Willow Crest Avenue<br>Animal Clinic</p>
  </div>
  <div class="photo photo--dogs" role="img" aria-label="Group of five dogs sitting together"></div>

  <div class="content" style="top:560px">
    <p class="lead">Advanced Orthopedic Care by Dr. Helena Pettigrew, DVM DACVS-SA<br><span class="lead--green">TPLO Surgery at Willow Crest Avenue Animal Clinic</span></p>
    <div class="cols">
      <div class="col">
        <h3 class="sec-h"><svg width="16" height="16" viewBox="0 0 16 16"><circle cx="8" cy="8" r="7" fill="var(--green)"/></svg>About Dr. Helena Pettigrew</h3>
        <p class="body">Dr. Helena Pettigrew is a board-certified veterinary surgeon (Diplomate of the National College of Veterinary Surgeons) with over 15 years of experience in small animal surgery. A graduate of Northfield State University, she completed her surgical residency at Eastbrook School of Veterinary Medicine. Through her mobile practice, Pettigrew Mobile Surgery, Dr. Pettigrew now provides advanced surgical procedures—such as TPLO—directly at local clinics.</p>
        <h3 class="sec-h"><svg width="16" height="16" viewBox="0 0 16 16"><circle cx="8" cy="8" r="7" fill="var(--green)"/></svg>What is TPLO Surgery?</h3>
        <p class="body">Tibial Plateau Leveling Osteotomy (TPLO) is a surgical procedure that stabilizes the stifle (knee) joint following a cranial cruciate ligament (CCL) rupture—a common orthopedic injury in dogs. The procedure involves altering the angle of the tibial plateau to eliminate abnormal joint motion, restoring stability and improving function.</p>
        <div class="xrays">
          <div class="xray xray--light" role="img" aria-label="Surgical model of a knee joint"></div>
          <div class="xray" role="img" aria-label="Radiograph of a stabilized knee"></div>
        </div>
      </div>
      <div class="col">
        <h3 class="sec-h"><svg width="16" height="16" viewBox="0 0 16 16"><circle cx="8" cy="8" r="7" fill="var(--green)"/></svg>Benefits of TPLO Surgery</h3>
        <div class="benefit"><h4>Enhanced Joint Stability:</h4><p>Restores natural biomechanics, reducing pain and improving mobility.</p></div>
        <div class="benefit"><h4>Faster Recovery:</h4><p>Many dogs return to normal activity faster compared to other surgical options.</p></div>
        <div class="benefit"><h4>Proven Long-Term Success:</h4><p>TPLO is particularly effective in large and active breeds.</p></div>
        <h3 class="sec-h"><svg width="16" height="16" viewBox="0 0 16 16"><circle cx="8" cy="8" r="7" fill="var(--green)"/></svg>Why Choose Willow Crest Avenue Animal Clinic?</h3>
        <p class="body">Partnering with Dr. Pettigrew, Willow Crest Avenue Animal Clinic offers advanced orthopedic surgery on-site—eliminating the need for referrals or travel. This collaboration ensures your pet receives expert surgical care in a familiar, trusted environment. Our clinic works directly with your primary veterinarian to share medical records, diagnostics, and prescriptions, ensuring seamless and coordinated care for your pet.</p>
      </div>
    </div>
  </div>

  <footer class="footer">
    <div class="footer__item"><span class="footer__icon"><svg width="12" height="12" viewBox="0 0 24 24"><path fill="#fff" d="M6.6 10.8a15 15 0 006.6 6.6l2.2-2.2c.3-.3.7-.4 1-.2 1.1.4 2.3.6 3.6.6.6 0 1 .4 1 1V20c0 .6-.4 1-1 1A17 17 0 013 4c0-.6.4-1 1-1h3.5c.6 0 1 .4 1 1 0 1.3.2 2.5.6 3.6.1.3 0 .7-.2 1z"/></svg></span>555-014-2270<br>555-014-2271</div>
    <div class="footer__item"><span class="footer__icon"><svg width="12" height="12" viewBox="0 0 24 24"><circle cx="12" cy="12" r="9" fill="none" stroke="#fff" stroke-width="2"/><path d="M3 12h18M12 3c3 3 3 15 0 18M12 3c-3 3-3 15 0 18" fill="none" stroke="#fff" stroke-width="1.5"/></svg></span>www.brookferrypetcare.com<br>www.northgroveanimalsurgery.com</div>
    <div class="footer__item"><span class="footer__icon"><svg width="12" height="12" viewBox="0 0 24 24"><path fill="#fff" d="M12 2a7 7 0 00-7 7c0 5 7 13 7 13s7-8 7-13a7 7 0 00-7-7zm0 9.5A2.5 2.5 0 1112 6a2.5 2.5 0 010 5.5z"/></svg></span>418 Willow Crest Ave, Fairhaven 40211</div>
    <div class="footer__item"><span class="footer__icon"><svg width="12" height="12" viewBox="0 0 24 24"><rect x="3" y="5" width="18" height="14" rx="2" fill="none" stroke="#fff" stroke-width="2"/><path d="M3 7l9 6 9-6" fill="none" stroke="#fff" stroke-width="2"/></svg></span>hello@brookferrypetcare.com<br>desk@northgroveanimalsurgery.com</div>
  </footer>
</section>

<!-- BACK -->
<section class="page page--back">
  <div class="brand-band"></div>
  <div class="brand"><span class="brand__mark"></span><span class="brand__name">Willow Crest Avenue Animal Clinic</span></div>
  <div class="badge" aria-hidden="true"></div>

  <span class="bubble" style="left:440px;top:56px;width:46px;height:46px"></span>
  <span class="bubble" style="left:490px;top:34px;width:28px;height:28px"></span>
  <span class="bubble" style="left:412px;top:96px;width:22px;height:22px"></span>
  <span class="bubble bubble--soft" style="left:740px;top:720px;width:110px;height:110px"></span>

  <div class="photo photo--surgery" role="img" aria-label="Surgical team operating in a clinic"></div>
  <div class="photo photo--paw" role="img" aria-label="Hand touching a small dog's raised paw at sunset"></div>

  <div class="content" style="top:580px">
    <h3 class="sec-h" style="font-size:15px"><svg width="16" height="16" viewBox="0 0 16 16"><circle cx="8" cy="8" r="7" fill="var(--green)"/></svg>Diagnostic Radiographs vs. TPLO Planning Radiographs</h3>
    <p class="intro">While diagnostic radiographs may confirm a CCL tear, they are not sufficient for surgical planning. TPLO requires three advanced technique radiographic views with precise measurements, which must be performed under sedation to reduce discomfort and allow accurate positioning.</p>

    <h3 class="sec-h" style="margin-top:22px"><svg width="16" height="16" viewBox="0 0 16 16"><circle cx="8" cy="8" r="7" fill="var(--green)"/></svg>Expected Process</h3>
    <div class="process">
      <div class="step"><span class="step__icon"><svg width="14" height="14" viewBox="0 0 24 24"><circle cx="11" cy="11" r="6" fill="none" stroke="var(--green)" stroke-width="2.5"/><path d="M16 16l5 5" stroke="var(--green)" stroke-width="2.5"/></svg></span><div><h4>Diagnosis</h4><p>Your pet is diagnosed with stifle instability (CCL tear) by your vet or at our clinic.</p></div></div>
      <div class="step"><span class="step__icon"><svg width="14" height="14" viewBox="0 0 24 24"><path d="M4 12h14M13 6l6 6-6 6" fill="none" stroke="var(--green)" stroke-width="2.5"/></svg></span><div><h4>Planning Radiographs</h4><p>Three specialized views are taken under sedation during the consultation visit.</p></div></div>
      <div class="step"><span class="step__icon"><svg width="14" height="14" viewBox="0 0 24 24"><rect x="4" y="4" width="16" height="16" rx="3" fill="none" stroke="var(--green)" stroke-width="2.5"/></svg></span><div><h4>Surgery Day</h4><p>Your pet is dropped off in the morning and surgery is performed the same day.</p></div></div>
      <div class="step"><span class="step__icon"><svg width="14" height="14" viewBox="0 0 24 24"><path d="M4 12h14M13 6l6 6-6 6" fill="none" stroke="var(--green)" stroke-width="2.5"/></svg></span><div><h4>Referral</h4><p>Your veterinarian forwards the records and exam findings to our clinic.</p></div></div>
      <div class="step"><span class="step__icon"><svg width="14" height="14" viewBox="0 0 24 24"><path d="M5 12l5 5 9-10" fill="none" stroke="var(--green)" stroke-width="2.5"/></svg></span><div><h4>Surgical Review</h4><p>Dr. Pettigrew reviews the radiographs and your pet's history to confirm TPLO.</p></div></div>
      <div class="step"><span class="step__icon"><svg width="14" height="14" viewBox="0 0 24 24"><path d="M5 12l5 5 9-10" fill="none" stroke="var(--green)" stroke-width="2.5"/></svg></span><div><h4>Discharge</h4><p>You'll receive a post-surgery update and your pet will go home that evening.</p></div></div>
      <div class="step"><span class="step__icon"><svg width="14" height="14" viewBox="0 0 24 24"><circle cx="12" cy="12" r="7" fill="none" stroke="var(--green)" stroke-width="2.5"/></svg></span><div><h4>Consultation</h4><p>The coordinator contacts you to schedule a visit and review the procedure and costs.</p></div></div>
      <div class="step"><span class="step__icon"><svg width="14" height="14" viewBox="0 0 24 24"><rect x="5" y="3" width="14" height="18" rx="2" fill="none" stroke="var(--green)" stroke-width="2.5"/></svg></span><div><h4>Deposit</h4><p>A deposit secures Dr. Pettigrew's travel and surgery date. It is non-refundable if cancelled late.</p></div></div>
    </div>

    <div class="postop" style="margin-top:24px">
      <h3 class="sec-h"><svg width="16" height="16" viewBox="0 0 16 16"><circle cx="8" cy="8" r="7" fill="var(--green)"/></svg>Post-Operative Care &amp; Follow-Up</h3>
      <p>Two follow-up appointments will be scheduled:</p>
      <p><b>2 Weeks Post-Op:</b> Evaluate healing, refill medications, and address any questions.</p>
      <p><b>8 Weeks Post-Op:</b> Sedated radiographs will confirm proper healing of the surgical site and plate.</p>
      <p>Dr. Pettigrew will stay in direct contact with you during your pet's recovery using the Dr. Pettigrew Mobile vet app, which allows for secure messaging and provides detailed post-operative instructions.</p>
    </div>
  </div>

  <footer class="footer">
    <div class="footer__item"><span class="footer__icon"><svg width="12" height="12" viewBox="0 0 24 24"><path fill="#fff" d="M6.6 10.8a15 15 0 006.6 6.6l2.2-2.2c.3-.3.7-.4 1-.2 1.1.4 2.3.6 3.6.6.6 0 1 .4 1 1V20c0 .6-.4 1-1 1A17 17 0 013 4c0-.6.4-1 1-1h3.5c.6 0 1 .4 1 1 0 1.3.2 2.5.6 3.6.1.3 0 .7-.2 1z"/></svg></span>555-014-2270<br>555-014-2271</div>
    <div class="footer__item"><span class="footer__icon"><svg width="12" height="12" viewBox="0 0 24 24"><circle cx="12" cy="12" r="9" fill="none" stroke="#fff" stroke-width="2"/><path d="M3 12h18M12 3c3 3 3 15 0 18M12 3c-3 3-3 15 0 18" fill="none" stroke="#fff" stroke-width="1.5"/></svg></span>www.brookferrypetcare.com<br>www.northgroveanimalsurgery.com</div>
    <div class="footer__item"><span class="footer__icon"><svg width="12" height="12" viewBox="0 0 24 24"><path fill="#fff" d="M12 2a7 7 0 00-7 7c0 5 7 13 7 13s7-8 7-13a7 7 0 00-7-7zm0 9.5A2.5 2.5 0 1112 6a2.5 2.5 0 010 5.5z"/></svg></span>418 Willow Crest Ave, Fairhaven 40211</div>
    <div class="footer__item"><span class="footer__icon"><svg width="12" height="12" viewBox="0 0 24 24"><rect x="3" y="5" width="18" height="14" rx="2" fill="none" stroke="#fff" stroke-width="2"/><path d="M3 7l9 6 9-6" fill="none" stroke="#fff" stroke-width="2"/></svg></span>hello@brookferrypetcare.com<br>desk@northgroveanimalsurgery.com</div>
  </footer>
</section>

</body>
</html>
```